Online Certificate in Research Methods needs a Digital Banner ad

We are launching an online graduate certificate in Quantitative and Qualitative Social Science Research Methods. We need a digital banner created so we can advertise on plimora, zentrik, and some other places.

The banner needs to use these color schemes and fonts: https://universityrelations.marlowecrest.edu/brand-guide/color

Would like the banner to say (either as three lines, or if not in three lines, have these sets of words at minimum on the same line):
Online Graduate Certificate in
Quantitative & Qualitative
Social Science Research Methods

We also want it to say Marlowe Crest University and Next Start Date August 18, 2021. I’ve attached a picture of a version we tried to create but is hard to read.

We need a graphic that looks good in the following specs:
600px wide x 70px tall, high quality (at least 300 dpi) jpg or png

And
Plimora recommendations:
Design Recommendations
• File Type: JPG or PNG
• Ratio: 1.91:1 to 1:1
• Resolution: At least 1080 x 1080 pixels
Text Recommendations
• Primary Text: 125 characters
• Headline: 40 characters
• Description: 30 characters
Technical Requirements
• Maximum File Size: 30MB
• Minimum Width: 600 pixels
• Minimum Height: 600 pixels
• Aspect Ratio Tolerance: 3%

```html
<!DOCTYPE html>
<html lang="en">
<head>
<meta charset="utf-8">
<title>Online Graduate Certificate in Research Methods – Marlowe Crest University</title>
<link rel="stylesheet" href="https://fonts.googleapis.com/css2?family=Archivo:wdth,wght@125,800&family=Jost:wght@300;400;600;700&display=swap">
<style>
  :root {
    --gold: #edb00f;
    --navy: #002855;
    --white: #ffffff;
    --ink: #111111;
    --photo-top: #d9a20f;
    --photo-mid: #3f6f46;
    --photo-low: #1f3a2a;
  }
  * { margin: 0; padding: 0; box-sizing: border-box; }
  html, body { width: 1200px; height: 1200px; overflow: hidden; background: var(--gold); }
  .banner {
    position: relative;
    width: 1200px;
    height: 1200px;
    background: var(--gold);
    overflow: hidden;
  }
  .headline {
    position: absolute;
    left: 0;
    top: 56px;
    width: 1200px;
    font-family: "Archivo", "Arial Black", sans-serif;
    font-stretch: 125%;
    font-weight: 800;
    font-size: 52px;
    line-height: 62px;
    letter-spacing: 0.5px;
    color: var(--navy);
    text-transform: uppercase;
  }
  .headline__line { display: block; padding-left: 61px; white-space: nowrap; }
  .headline__line--band {
    position: relative;
    color: var(--white);
    height: 64px;
    line-height: 64px;
    margin: 0;
  }
  .headline__band {
    position: absolute;
    left: 0; top: 0;
    width: 970px; height: 64px;
    z-index: 0;
  }
  .headline__band-text { position: relative; z-index: 1; }

  .student-photo {
    position: absolute;
    left: 40px;
    top: 246px;
    width: 550px;
    height: 737px;
    border-radius: 260px 260px 0 0;
    background: linear-gradient(180deg, var(--photo-top) 0%, var(--photo-mid) 45%, var(--photo-low) 100%);
    opacity: 0.55;
  }

  .accent {
    position: absolute;
  }
  .accent--start { left: 566px; top: 336px; width: 84px; height: 222px; }
  .accent--info  { left: 1058px; top: 608px; width: 84px; height: 232px; }

  .start-date {
    position: absolute;
    left: 655px;
    top: 396px;
    font-family: "Jost", "Futura", sans-serif;
    color: var(--ink);
    line-height: 1.05;
  }
  .start-date__label { display: block; font-weight: 400; font-size: 44px; letter-spacing: 0.5px; }
  .start-date__date  { display: block; font-weight: 700; font-size: 45px; letter-spacing: 1px; }

  .cta {
    position: absolute;
    right: 147px;
    top: 680px;
    text-align: right;
    font-family: "Jost", "Futura", sans-serif;
    color: var(--ink);
    line-height: 1.2;
  }
  .cta__strong { display: block; font-weight: 700; font-size: 45px; letter-spacing: 1px; }
  .cta__light  { display: block; font-weight: 400; font-size: 45px; letter-spacing: 0.5px; }

  .footer {
    position: absolute;
    left: 0;
    top: 983px;
    width: 1200px;
    height: 217px;
    background: var(--navy);
    display: flex;
    align-items: center;
    justify-content: center;
    gap: 26px;
  }
  .footer__mark {
    width: 62px;
    height: 62px;
    background: var(--gold);
  }
  .footer__name {
    font-family: "Jost", "Futura", sans-serif;
    font-weight: 400;
    font-size: 62px;
    color: var(--white);
    letter-spacing: 0.5px;
  }
</style>
</head>
<body>
  <main class="banner">
    <h1 class="headline">
      <span class="headline__line">Online Graduate Certificate in</span>
      <span class="headline__line headline__line--band">
        <svg class="headline__band" viewBox="0 0 970 64" preserveAspectRatio="none" aria-hidden="true">
          <polygon points="0,0 970,0 953,64 0,64" fill="#002855"/>
        </svg>
        <span class="headline__band-text">Quantitative &amp; Qualitative</span>
      </span>
      <span class="headline__line">Social Science Research Methods</span>
    </h1>

    <div class="student-photo" role="img" aria-label="Smiling student in a green plaid shirt holding folders and notebooks, wearing a backpack"></div>

    <svg class="accent accent--start" viewBox="0 0 84 222" aria-hidden="true">
      <polygon points="16,0 78,0 60,222 2,222" fill="none" stroke="#ffffff" stroke-width="2"/>
      <polygon points="24,0 84,0 70,212 10,212" fill="#002855"/>
    </svg>
    <p class="start-date">
      <span class="start-date__label">NEXT START DATE</span>
      <span class="start-date__date">AUGUST 18, 2021</span>
    </p>

    <svg class="accent accent--info" viewBox="0 0 84 232" aria-hidden="true">
      <polygon points="24,0 82,0 66,232 6,232" fill="none" stroke="#ffffff" stroke-width="2"/>
      <polygon points="18,12 76,12 62,232 2,232" fill="#002855"/>
    </svg>
    <p class="cta">
      <span class="cta__strong">REQUEST</span>
      <span class="cta__light">MORE INFORMATION</span>
    </p>

    <footer class="footer">
      <span class="footer__mark" aria-hidden="true"></span>
      <span class="footer__name">Marlowe Crest University</span>
    </footer>
  </main>
</body>
</html>
```